Business Card Design Project

We need a business card design for a new construction company called 'KORVA HOLDINGS PTY.LTD' We run a construction based company for high end market homes in melbourne, we want something that looks professional and eye catching.The card needs to have a strong design to it something modern as the company name explains "korva." The final design should communicate professionalism and a strong image to our customers on the quality of our work.
On the business card i need
Name: Marek Holtvay
Mob:0417295031
Email:korva.holdings@mailbrook.example
Domestic/Residential/Commercial

```html
<!DOCTYPE html>
<html lang="en">
<head>
<meta charset="utf-8">
<title>Korva Holdings – Business Card</title>
<link rel="stylesheet" href="https://fonts.googleapis.com/css2?family=Open+Sans:wght@400;600;700&display=swap">
<style>
  :root {
    --stage: #e9e7e4;
    --card: #f7f7f7;
    --ink: #2e2e30;
    --muted: #6b6b6e;
    --red: #e0193a;
    --red-soft: #ef4463;
    --white: #ffffff;
  }
  * { box-sizing: border-box; margin: 0; padding: 0; }
  html, body { width: 1200px; height: 900px; overflow: hidden; }
  body {
    background: var(--stage);
    font-family: "Open Sans", Arial, sans-serif;
    position: relative;
  }
  .card {
    position: absolute;
    left: 320px;
    width: 560px;
    height: 320px;
    background: var(--card);
    box-shadow: 0 10px 28px rgba(0,0,0,0.14);
    overflow: hidden;
  }
  .card--back { top: 95px; }
  .card--front { top: 485px; }

  /* back */
  .back-strip {
    position: absolute; left: 0; top: 0;
    width: 16px; height: 120px;
    background: var(--red);
  }
  .back-logo {
    position: absolute; left: 0; right: 0; top: 96px;
    text-align: center;
  }
  .back-logo .wordmark { font-size: 100px; }
  .back-logo .company { font-size: 15px; margin-top: 6px; }

  /* shared logo */
  .wordmark {
    font-weight: 600;
    color: var(--ink);
    line-height: 1;
  }
  .company {
    color: var(--ink);
    font-weight: 400;
    text-transform: uppercase;
  }

  /* front */
  .contact-panel {
    position: absolute; left: 0; top: 0;
    width: 240px; height: 196px;
    background: linear-gradient(135deg, var(--red) 0%, var(--red-soft) 100%);
    border-bottom-right-radius: 34px;
    color: var(--white);
    padding: 92px 0 0 26px;
  }
  .contact-panel .person { font-size: 17px; font-weight: 700; }
  .contact-panel .label { font-size: 11px; margin-top: 12px; letter-spacing: 0.5px; }
  .contact-panel .phone { font-size: 13px; margin-top: 2px; letter-spacing: 0.5px; }

  .front-logo {
    position: absolute; left: 290px; top: 112px;
    width: 240px;
    text-align: center;
  }
  .front-logo .wordmark { font-size: 50px; }
  .front-logo .company { font-size: 10px; margin-top: 4px; }

  .services {
    position: absolute; left: 290px; top: 206px;
    width: 240px;
    text-align: center;
    font-size: 11px;
    color: var(--muted);
  }

  .edge-strip {
    position: absolute; right: 0;
    width: 14px; height: 92px;
    background: var(--red);
  }
  .edge-strip--top { top: 0; }
  .edge-strip--bottom { bottom: 0; }

  .email {
    position: absolute; left: 26px; bottom: 24px;
    font-size: 12.5px;
    color: var(--red);
  }
</style>
</head>
<body>

  <section class="card card--back" aria-label="Card back">
    <div class="back-strip"></div>
    <div class="back-logo">
      <div class="wordmark">korva</div>
      <div class="company">Korva Holdings Pty.Ltd</div>
    </div>
  </section>

  <section class="card card--front" aria-label="Card front">
    <div class="contact-panel">
      <p class="person">Marek Holtvay</p>
      <p class="label">PHONE</p>
      <p class="phone">0417295031</p>
    </div>
    <div class="front-logo">
      <div class="wordmark">korva</div>
      <div class="company">Korva Holdings Pty.Ltd</div>
    </div>
    <p class="services">Domestic / Residential / Commercial</p>
    <div class="edge-strip edge-strip--top"></div>
    <div class="edge-strip edge-strip--bottom"></div>
    <p class="email">korva.holdings@mailbrook.example</p>
  </section>

</body>
</html>
```